Doppelseite in einer Zeitschrift
Zielgruppe
Hallo Zusammen
Unser Unternehmen hat in einer Zeitschrift eine Doppelseite gebucht (2x A4)
Wir haben schon das Foto, den Text und das Logo dazu.
Was wir noch brauchen ist, diese drei Komponenten in ein schönes Design zu kriegen.
Wichtig ist, in der Mitte wird der Falz von der Zeitschrift sein, aus diesem Grund muss ein Teil vom Text auf der Linken und der andere Teil auf der Rechten Seite sein.
Zusätzlich kann beim Foto der Text unten rechts 'Basel' komplett entfernt werden.
Falls jemand noch ein Muster senden kann, mit einem anderen Foto (Stadtbild von Basel oder einer Vogelperspektive, dann sehr gerne)
Aufgabenstellung
Es soll einen modernen Eindruck hinterlassen.

```html
<!DOCTYPE html>
<html lang="de">
<head>
<meta charset="utf-8">
<title>Domavera AG – Doppelseite</title>
<link rel="stylesheet" href="https://fonts.googleapis.com/css2?family=Ubuntu:wght@400;500;700&family=Playfair+Display:ital,wght@0,400;1,400&display=swap">
<style>
:root{
  --red:#d6121f;
  --ink:#3b3b3b;
  --ink-soft:#4a4a4a;
  --rule:#c9c9c9;
  --panel:#e7f1f0;
  --stage:#efefef;
  --paper:#ffffff;
  --sans:"Ubuntu", Arial, sans-serif;
  --serif:"Playfair Display", Georgia, serif;
}
*{margin:0;padding:0;box-sizing:border-box}
html,body{width:849px;height:1200px;overflow:hidden;background:var(--stage)}
.stage{position:relative;width:849px;height:1200px}
.spread-frame{position:absolute;left:14px;top:313px;width:820px;height:574px}
.spread{position:absolute;left:0;top:0;width:1134px;height:794px;background:var(--paper);
  transform:scale(.7231);transform-origin:0 0;overflow:hidden;font-family:var(--sans);color:var(--ink)}
.brand{position:absolute;left:27px;top:22px;font-family:var(--sans);font-size:21px;font-weight:400;color:var(--ink-soft);line-height:24px}
.top-rule{position:absolute;left:27px;right:27px;top:50px;border-top:1px solid var(--rule)}
.headline{position:absolute;left:27px;top:64px;font-size:42px;line-height:43px;font-weight:700;color:var(--red);white-space:nowrap}
.subline{position:absolute;left:27px;top:156px;font-size:28px;font-weight:500;color:var(--ink-soft);white-space:nowrap}
.body{font-size:9.4px;line-height:15.2px;color:var(--ink);hyphens:auto;-webkit-hyphens:auto}
.col{position:absolute;width:254px}
.col-a{left:27px;top:206px}
.col-b{left:290px;top:206px}
.photo{position:absolute;left:0;top:343px;width:1134px;height:451px;
  background:
   linear-gradient(180deg,rgba(228,242,238,1) 0%,rgba(228,242,238,0) 22%),
   linear-gradient(100deg,#7b7060 0%,#5f8a3c 14%,#6e9648 28%,#8aa15c 40%,#a8b9a4 50%,#4fc2c3 60%,#2fb4b7 80%,#3bbdbb 100%)}
.right-cover{position:absolute;left:567px;top:343px;width:290px;height:205px;background:var(--paper)}
.right-head{position:absolute;left:594px;top:80px;font-size:20px;font-weight:500;color:var(--ink-soft);white-space:nowrap}
.col-r{position:absolute;left:594px;width:254px}
.intro{top:126px}
.dots{position:absolute;left:594px;width:250px;border-top:1px dotted var(--red)}
.quote{position:absolute;left:594px;top:226px;width:250px;text-align:center;font-family:var(--serif);
  font-size:15px;line-height:23px;color:var(--red)}
.services-text{top:342px}
.closing{top:468px}
.panel{position:absolute;left:857px;top:125px;width:277px;height:440px;
  background:linear-gradient(180deg,var(--panel) 0%,var(--panel) 88%,rgba(231,241,240,0) 100%)}
.skyline{position:absolute;left:12px;top:0;width:260px;height:75px;
  background:linear-gradient(180deg,rgba(231,241,240,0) 0%,#5b6670 55%,#9fb1b4 100%);opacity:.85}
.panel-title{position:absolute;left:0;top:86px;width:277px;text-align:center;font-family:var(--serif);
  font-size:22px;line-height:29px;font-weight:400;color:var(--ink-soft)}
.service{position:absolute;width:128px;text-align:center}
.service-name{font-size:9px;letter-spacing:1px;font-weight:500;color:var(--ink-soft)}
.service-icon{display:block;margin:7px auto 6px}
.service-note{font-size:6.3px;line-height:9px;color:var(--ink)}
.caption{position:absolute;top:722px;font-family:var(--serif);font-style:italic;font-size:31px;color:#fff;white-space:nowrap}
</style>
</head>
<body>
<main class="stage">
 <div class="spread-frame">
  <article class="spread">
   <div class="photo" role="img" aria-label="Foto: Basler Altstadt am Rhein mit Münster, grünen Bäumen und türkisem Fluss"></div>
   <div class="right-cover"></div>

   <div class="brand">Domavera AG</div>
   <div class="top-rule"></div>

   <h1 class="headline">Domavera AG: Gemeinsam<br>Werte pflegen –</h1>
   <h2 class="subline">Ein Dankeschön an unsere Partner</h2>

   <p class="body col col-a">Seit 2005 dürfen wir, die Domavera AG, Sie als unsere geschätzten Kundinnen und Kunden begleiten und für Ihre Immobilien da sein. Diese langjährige Partnerschaft erfüllt uns mit Stolz und Dankbarkeit. Es ist uns ein Anliegen, Ihnen mit diesem Beitrag einmal mehr zu zeigen, wofür wir stehen und wie wir uns gemeinsam mit Ihnen für den Werterhalt und die Pflege Ihrer Liegenschaften einsetzen – mit Sorgfalt, Herz und einem Blick für die Zukunft.</p>
   <p class="body col col-b">In einer vertrauensvollen Zusammenarbeit haben wir über die Jahre viele Veränderungen miterlebt und gemeinsam gemeistert.<br>Es ist dem Team der Domavera AG ein tägliches Bestreben, Ihnen nicht nur einen erstklassigen Service zu bieten, sondern dies auch auf eine Weise zu tun, die unsere gemeinsamen Werte widerspiegelt: Verantwortung für unsere Umwelt und ein respektvolles Miteinander.</p>

   <h2 class="right-head">Ein Blick nach vorn – Gemeinsam in die Zukunft</h2>
   <p class="body col-r intro">Als Ihr verlässlicher Partner für Liegenschaften möchten wir uns herzlich für Ihre Treue und die gute Zusammenarbeit bedanken. Die Domavera AG ist mehr als nur ein Dienstleister – wir sind ein eingespieltes Team für Ihre Liegenschaft.</p>
   <div class="dots" style="top:215px"></div>
   <blockquote class="quote">„Werte lassen sich nicht ersetzen.<br>Man kann sie nur pflegen –<br>gemeinsam, mit Vertrauen<br>und Beständigkeit.“</blockquote>
   <div class="dots" style="top:325px"></div>
   <p class="body col-r services-text">Ob Hauswartung, Gartenpflege, Reinigung oder Räumungen – Sie kennen unser breites Dienstleistungsspektrum. Unser Team ist bestens eingespielt und mit Herz bei der Sache, um für jede Ihrer Liegenschaften die beste Lösung zu finden. Die langjährige Erfahrung und die tiefe Verbundenheit mit der Region Basel sind das Fundament, auf dem unsere vertrauensvolle Partnerschaft ruht.</p>
   <p class="body col-r closing">Wir freuen uns darauf, auch in Zukunft gemeinsam mit Ihnen für ein gepflegtes und lebenswertes Umfeld zu sorgen und die Werte zu pflegen, die uns verbinden.</p>

   <aside class="panel">
    <div class="skyline" role="img" aria-label="Illustration: Silhouette der Stadt Basel"></div>
    <h3 class="panel-title">Unser Engagement<br>in der Region Basel</h3>

    <div class="service" style="left:4px;top:166px">
     <div class="service-name">HAUSWARTUNG</div>
     <svg class="service-icon" width="60" height="60" viewBox="0 0 60 60"><circle cx="30" cy="30" r="29" fill="none" stroke="#4a5560" stroke-width="1.2"/></svg>
     <p class="service-note">Zuverlässige Betreuung Ihrer Liegenschaft – sorgfältig, präsent und vorausschauend.</p>
    </div>
    <div class="service" style="left:144px;top:166px">
     <div class="service-name">GARTENPFLEGE</div>
     <svg class="service-icon" width="60" height="60" viewBox="0 0 60 60"><circle cx="30" cy="30" r="29" fill="none" stroke="#4a5560" stroke-width="1.2"/></svg>
     <p class="service-note">Gepflegte Aussenanlagen, die Eindruck machen – fachgerecht, saisonal und nachhaltig.</p>
    </div>
    <div class="service" style="left:4px;top:296px">
     <div class="service-name">WOHNUNGSREINIGUNG</div>
     <svg class="service-icon" width="60" height="60" viewBox="0 0 60 60"><circle cx="30" cy="30" r="29" fill="none" stroke="#4a5560" stroke-width="1.2"/></svg>
     <p class="service-note">Gründliche Reinigung bei Mieterwechsel für eine reibungslose Übergabe und einen perfekten Neustart.</p>
    </div>
    <div class="service" style="left:144px;top:296px">
     <div class="service-name">WOHNUNGSRÄUMUNG</div>
     <svg class="service-icon" width="60" height="60" viewBox="0 0 60 60"><circle cx="30" cy="30" r="29" fill="none" stroke="#4a5560" stroke-width="1.2"/></svg>
     <p class="service-note">Sorgsame Wohnungsauflösungen bei Umzug, Pflege oder Nachlassregelung.</p>
    </div>
   </aside>

   <p class="caption" style="left:292px">Regional verwurzelt.</p>
   <p class="caption" style="left:594px">Gemeinsam für gepflegte Liegenschaften.</p>
  </article>
 </div>
</main>
</body>
</html>
```